5-star Hotel Web Design Project

I need a custom website design for a 5-star hotel. For full details please look at the attached ZIP archive.

The design should be in layers in Photoshop/Illustrator/InDesign format with all the icons/shapes/maps/graphic assets in vector format (svg, ai, eps) as much as possible.

I prefer white, simple but elegant websites. Please consider the performance/coding experience. We're not making something to show off our design skills on a design contest with fancy parallax effects and confusing animations. We're trying to create usable, functional and clean UI with good UX.

I would like to receive a few option for the color scheme to choose from.

The website will be custom coded, i.e. I'm not using WordPress.

NOTE: Don't bother to submit the generic WordPress style templates. We're looking for something custom made with attention to details. That's why the price is not guaranteed, but don't be mistaken, I'm a long time buyer here on FolioBazaar and all my projects are paid in full.
Updates

Low design quality

Target Market(s)

Europe

Industry/Entity Type

Hotel

Number of Pages Required

5+ page

```html
<!DOCTYPE html>
<html lang="en">
<head>
<meta charset="utf-8">
<title>Coral Bay Resort</title>
<link href="https://fonts.googleapis.com/css2?family=Josefin+Sans:wght@600;700&family=Poppins:wght@400;500;600;700&display=swap" rel="stylesheet">
<style>
:root{
  --crimson:#a5103b;
  --gold:#d4a95a;
  --ink:#2b2b2b;
  --muted:#8a8a8a;
  --soft:#f5f5f5;
  --navy:#1c3457;
  --dark:#2d2d2d;
  --white:#fff;
}
*{box-sizing:border-box;margin:0;padding:0}
html,body{width:1200px;height:5080px;overflow:hidden}
body{position:relative;font-family:"Poppins",sans-serif;color:var(--ink);background:var(--white);font-size:13px}
.abs{position:absolute}
.heading{font-family:"Josefin Sans",sans-serif;font-weight:700}
.btn{position:absolute;display:flex;align-items:center;justify-content:center;border-radius:30px;background:var(--crimson);color:var(--white);font-weight:600;font-size:14px;box-shadow:0 8px 18px rgba(165,16,59,.3)}
.btn-outline{position:absolute;display:flex;align-items:center;justify-content:center;border:1.5px solid #555;border-radius:20px;font-size:12px;width:106px;height:34px;color:var(--ink)}
.eyebrow{color:var(--crimson);font-size:17px}
.photo{position:absolute}

/* top bar */
.topbar{position:absolute;left:0;top:0;width:1200px;height:30px;background:var(--crimson);color:var(--white);font-size:11px}
.topbar span{position:absolute;top:8px}
.dot{display:inline-block;width:9px;height:9px;border-radius:50%;background:var(--white);margin-left:6px;vertical-align:middle}

/* hero */
.hero{left:0;top:30px;width:1200px;height:570px;background:linear-gradient(180deg,#b9b09a 0%,#8aa49a 35%,#3f8f88 70%,#2f7d78 100%)}
.hero-figure{left:780px;top:30px;width:420px;height:570px;background:linear-gradient(90deg,rgba(233,184,150,0) 0%,rgba(226,170,138,.85) 40%,rgba(240,180,170,.9) 100%)}
.brand{font-family:"Poppins",sans-serif;font-weight:500;color:var(--white);font-size:17px}
.main-nav{position:absolute;left:458px;top:62px;display:flex;gap:26px}
.main-nav a{color:var(--white);font-size:14px;text-decoration:none;white-space:nowrap}
.login{position:absolute;left:922px;top:52px;width:93px;height:38px;border:1.5px solid var(--white);border-radius:20px;color:var(--white);display:flex;align-items:center;justify-content:center;font-size:15px}
.hero-title{left:184px;top:178px;color:var(--white);font-size:54px;line-height:1.12;letter-spacing:2px}
.hero-text{left:184px;top:318px;width:330px;color:var(--white);font-size:14px;line-height:1.55}

.booking{left:276px;top:537px;width:648px;height:108px;background:var(--white);box-shadow:0 10px 30px rgba(0,0,0,.12)}
.field{position:absolute;top:36px}
.field b{display:block;font-size:14px;font-weight:600}
.field small{display:block;font-size:12px;color:var(--muted);margin-top:6px}
.field svg{position:absolute;right:-22px;top:6px}

/* about */
.about-title{left:628px;top:770px;font-size:31px;line-height:1.35;letter-spacing:1px}
.about-text{left:628px;top:870px;width:360px;font-size:14px;line-height:1.65}
.badge{position:absolute;top:980px;width:104px;height:145px;background:var(--white);box-shadow:0 4px 14px rgba(0,0,0,.12);padding:10px}
.badge i{display:block;width:100%;height:100%;background:#eceff2;border-radius:2px}

/* offers */
.offers{left:0;top:1306px;width:1200px;height:1412px;background:var(--soft)}
.center{left:0;width:1200px;text-align:center}
.section-title{font-size:29px;letter-spacing:1px}
.card{position:absolute;width:260px}
.card .img{position:relative;height:310px}
.price{position:absolute;right:0;bottom:0;width:96px;height:64px;background:var(--soft);color:var(--gold);font-weight:600;font-size:20px;display:flex;align-items:center;justify-content:center}
.card h3{margin-top:26px;font-size:18px;font-weight:600;display:flex;align-items:center;gap:16px;white-space:nowrap}
.rate{display:inline-block;background:#fbeed5;color:var(--gold);font-size:9px;font-weight:500;padding:2px 10px;border-radius:10px}
.card p{margin-top:14px;font-size:14px;line-height:1.6;color:#666;width:270px}
.card .btn-outline{position:relative;margin-top:16px}

/* testimonial */
.testi-title{left:582px;top:2846px;font-size:31px;letter-spacing:1px}
.quote-text{left:582px;top:2944px;width:380px;font-size:13px;line-height:1.75;color:var(--muted)}
.arrows{left:440px;top:3200px;width:89px;height:49px;background:var(--white);display:flex;align-items:center;justify-content:center;gap:14px}

/* benefits */
.benefits{left:0;top:3332px;width:1200px;height:413px;background:linear-gradient(180deg,#22395b 0%,#1b3354 60%,#213c60 100%)}
.circle-btn{position:absolute;top:3413px;width:38px;height:38px;border-radius:50%;display:flex;align-items:center;justify-content:center}
.features{left:184px;top:3534px;width:832px;height:355px;background:var(--white);box-shadow:0 10px 30px rgba(0,0,0,.08)}
.feature{position:absolute;width:186px;height:150px;display:flex;flex-direction:column;align-items:center;justify-content:center;text-align:center;font-size:13px;font-weight:600;gap:18px}
.feature.active{box-shadow:0 6px 22px rgba(0,0,0,.1);color:var(--crimson);background:var(--white)}
.vline{position:absolute;width:1px;background:#eee}

/* accommodation */
.room{position:absolute;top:4094px;width:405px;height:275px;background:var(--white);box-shadow:0 6px 24px rgba(0,0,0,.1)}
.room .info{position:absolute;top:28px;width:170px}
.room h4{font-size:18px;font-weight:600;line-height:1.4}
.room .rate-line{font-size:15px;margin-top:8px;white-space:nowrap}
.room .rate-line small{font-size:10px}
.room ul{list-style:none;margin-top:12px;font-size:12px}
.room li{margin-bottom:6px}
.room li::before{content:"\2713";margin-right:8px}
.room .more{margin-top:6px;width:88px;height:30px;border:1.5px solid #999;border-radius:16px;font-size:11px;display:flex;align-items:center;justify-content:center}

/* footer */
.footer{left:0;top:4560px;width:1200px;height:520px;background:var(--dark);color:var(--white)}
.news-title{left:184px;top:4652px;font-family:"Poppins",sans-serif;font-weight:700;font-size:29px;line-height:1.35;color:var(--white)}
.news-box{left:592px;top:4635px;width:424px;height:70px;background:var(--white);border-radius:36px}
.col{position:absolute;top:4800px;font-size:12px;color:#ddd}
.col h5{font-size:14px;font-weight:600;color:var(--white);margin-bottom:28px}
.col > div{margin-bottom:15px;white-space:nowrap}
.contact-row{display:flex;gap:14px;align-items:flex-start}
.contact-row .ico{width:12px;flex:none;text-align:center}
.copy{left:0;top:5024px;width:1200px;text-align:center;font-size:11px;color:#ccc}
</style>
</head>
<body>

<!-- top bar -->
<div class="topbar">
  <span style="left:184px">&#9742;&nbsp;&nbsp;+00 555 0142 80</span>
  <span style="left:340px">&#9993;&nbsp;&nbsp;hello@coralbayresort.example</span>
  <span style="left:790px">Stay Connected : <i class="dot"></i><i class="dot"></i><i class="dot"></i><i class="dot"></i></span>
  <span style="left:990px">EN &#9662;</span>
</div>

<!-- hero -->
<div class="photo hero" role="img" aria-label="Guest relaxing at the edge of a sunlit swimming pool"></div>
<div class="photo hero-figure" role="img" aria-label="Woman in sunglasses by the pool"></div>
<div class="abs brand" style="left:184px;top:58px"><span class="dot" style="margin:0 8px 0 0;width:12px;height:12px"></span>Coral Bay Resort</div>
<nav class="main-nav">
  <a>Coral Bay</a><a>Book direct</a><a>Special Offers</a><a>Location</a>
</nav>
<div class="login">Login</div>
<h1 class="abs heading hero-title">Book Direct With<br>20% Discount</h1>
<p class="abs hero-text">Lorem ipsum dolor sit amet, consectetur adipiscing elit sed do eiusmod.</p>
<div class="btn" style="left:184px;top:394px;width:142px;height:50px">Book Now!</div>

<div class="abs booking">
  <div class="field" style="left:34px"><b>Check In</b><small>21/04/2021</small>
    <svg width="10" height="6"><path d="M1 1l4 4 4-4" stroke="#333" fill="none"/></svg></div>
  <div class="field" style="left:162px"><b>Check Out</b><small>23/04/2021</small>
    <svg width="10" height="6"><path d="M1 1l4 4 4-4" stroke="#333" fill="none"/></svg></div>
  <div class="field" style="left:310px"><b>Guest And Room</b><small>Add guests and room</small>
    <svg width="10" height="6"><path d="M1 1l4 4 4-4" stroke="#333" fill="none"/></svg></div>
  <div class="btn" style="left:504px;top:34px;width:106px;height:42px;font-size:14px">Check</div>
</div>

<!-- about -->
<div class="photo" style="left:184px;top:728px;width:404px;height:217px;background:linear-gradient(135deg,#c9b79a,#8f7558 55%,#e6dccb)" role="img" aria-label="Bright hotel bedroom with twin beds"></div>
<div class="photo" style="left:184px;top:960px;width:191px;height:225px;background:linear-gradient(160deg,#1f4aa0,#12275e 60%,#b02020)" role="img" aria-label="Illuminated hotel sign against a blue sky"></div>
<div class="photo" style="left:397px;top:960px;width:191px;height:265px;background:linear-gradient(160deg,#2f5e3a,#3d8f86 50%,#26472c)" role="img" aria-label="Aerial view of a pool among tropical trees"></div>
<div class="abs eyebrow" style="left:628px;top:726px">About us</div>
<h2 class="abs heading about-title">Make Yourself at home<br>in our Hotel</h2>
<p class="abs about-text">Lorem ipsum dolor sit amet, consectetur adipiscing elit, sed do eiusod tempor incididut labore et dolore magna aliqua.</p>
<div class="badge" style="left:624px"><i></i></div>
<div class="badge" style="left:758px"><i style="background:#efe4d3"></i></div>
<div class="badge" style="left:886px"><i style="background:#e8eef5"></i></div>
<div class="btn" style="left:628px;top:1176px;width:142px;height:50px">Read More</div>

<!-- offers -->
<div class="abs offers"></div>
<div class="abs center eyebrow" style="top:1388px">Best Deals</div>
<h2 class="abs center heading section-title" style="top:1436px">Most Popular Offers</h2>

<div class="card" style="left:184px;top:1530px">
  <div class="img" style="background:linear-gradient(135deg,#f1ece8,#e4d6d4 55%,#c9b7a0)" role="img" aria-label="Easter table setting with ribbon and willow branches"><div class="price">$499</div></div>
  <h3>Easter Offer <span class="rate">&#9733; 4.5</span></h3>
  <p>Lorem ipsum dolor sit amet, consectetur adipiscing elit, sed</p>
  <div class="btn-outline">Book Now!</div>
</div>
<div class="card" style="left:468px;top:1530px">
  <div class="img" style="background:linear-gradient(180deg,#6fa6d0,#e6eef2 40%,#4b7d52 60%,#5fc7d0)" role="img" aria-label="Palm-lined resort swimming pool"><div class="price">$459</div></div>
  <h3>Summer Offer <span class="rate">&#9733; 4.5</span></h3>
  <p>Lorem ipsum dolor sit amet, consectetur adipiscing elit, sed</p>
  <div class="btn-outline">Book Now!</div>
</div>
<div class="card" style="left:752px;top:1530px">
  <div class="img" style="background:linear-gradient(135deg,#3a4f66,#a4b8cc 45%,#d9d3c8)" role="img" aria-label="Hotel room with city skyline view"><div class="price">$399</div></div>
  <h3>Early Bookings 2021 <span class="rate">&#9733; 4.5</span></h3>
  <p>Lorem ipsum dolor sit amet, con sectetur adipiscing elit, do eiu</p>
  <div class="btn-outline">Book Now!</div>
</div>

<div class="card" style="left:184px;top:2040px">
  <div class="img" style="background:linear-gradient(135deg,#d8d4cf,#2b2b2b 55%,#c7a45c)" role="img" aria-label="New Year letter board with gold balloons"><div class="price">$399</div></div>
  <h3>New Year Offer <span class="rate">&#9733; 4.5</span></h3>
  <p>Lorem ipsum dolor sit amet, consectetur adipiscing elit, sed</p>
  <div class="btn-outline">Book Now!</div>
</div>
<div class="card" style="left:468px;top:2040px">
  <div class="img" style="background:linear-gradient(135deg,#f3c9cf,#f6d7da 50%,#eab8bf)" role="img" aria-label="Pine cones and letter tiles on pink background"><div class="price">$199</div></div>
  <h3>Christmas Offer <span class="rate">&#9733; 4.5</span></h3>
  <p>Lorem ipsum dolor sit amet, consectetur adipiscing elit, sed</p>
  <div class="btn-outline">Book Now!</div>
</div>
<div class="card" style="left:752px;top:2040px">
  <div class="img" style="background:linear-gradient(180deg,#dfe4e6,#b7c2c4 45%,#c9b59a)" role="img" aria-label="Friends running into the sea on a beach"><div class="price">$259</div></div>
  <h3>Weekend Offer <span class="rate">&#9733; 4.5</span></h3>
  <p>Lorem ipsum dolor sit amet, con sectetur adipiscing elit, do eiu</p>
  <div class="btn-outline">Book Now!</div>
</div>
<div class="btn" style="left:529px;top:2584px;width:142px;height:50px">View More</div>

<!-- testimonial -->
<div class="photo" style="left:184px;top:2797px;width:345px;height:452px;background:linear-gradient(170deg,#6d7e8c,#3c5f79 35%,#c9c5bf 70%,#e7e4df)" role="img" aria-label="Guest wrapped in blankets looking out over the sea from a hotel room"></div>
<div class="abs arrows">
  <svg width="22" height="10"><path d="M21 5H2M6 1L2 5l4 4" stroke="#999" fill="none"/></svg>
  <svg width="22" height="10"><path d="M1 5h19M16 1l4 4-4 4" stroke="#a5103b" fill="none" stroke-width="1.5"/></svg>
</div>
<div class="abs eyebrow" style="left:582px;top:2792px">Testimonial</div>
<h2 class="abs heading testi-title">What People Say</h2>
<div class="abs" style="left:582px;top:2904px;font-size:14px;font-weight:500">" Great Service "</div>
<p class="abs quote-text">One of the best hotel in kormangla it was a good stay worm welcome ,hospitalible staff,polite&amp;cooperative behaviour of thehotel staff good rooms with all basic amenities that you require.Best part is hotel is located in prime location of Koramangala easily accessible to all the restaurants and party</p>
<div class="abs" style="left:582px;top:3104px;font-size:17px;font-weight:600">Elena Marsh</div>
<div class="abs" style="left:582px;top:3132px;font-size:12px;color:#666">Satisfied Customer</div>
<div class="photo" style="left:582px;top:3168px;width:68px;height:68px;border-radius:50%;background:linear-gradient(135deg,#e8c36c,#b8772e)" role="img" aria-label="Customer portrait"></div>

<!-- benefits -->
<div class="photo benefits" role="img" aria-label="Hotel exterior at dusk with navy overlay"></div>
<div class="abs" style="left:184px;top:3410px;color:#fff;font-size:17px">Our Benefits</div>
<h2 class="abs heading" style="left:184px;top:3456px;color:#fff;font-size:30px;letter-spacing:1px">Our Top Features</h2>
<div class="circle-btn" style="left:918px;border:1.5px solid rgba(255,255,255,.7)">
  <svg width="8" height="12"><path d="M7 1L2 6l5 5" stroke="#fff" fill="none"/></svg></div>
<div class="circle-btn" style="left:978px;background:var(--crimson)">
  <svg width="8" height="12"><path d="M1 1l5 5-5 5" stroke="#fff" fill="none"/></svg></div>

<div class="abs features">
  <div class="vline" style="left:232px;top:30px;height:140px"></div>
  <div class="vline" style="left:604px;top:30px;height:140px"></div>
  <div class="vline" style="left:232px;top:185px;height:140px"></div>
  <div class="vline" style="left:418px;top:185px;height:140px"></div>
  <div class="vline" style="left:604px;top:185px;height:140px"></div>
  <div class="feature" style="left:44px;top:30px">
    <svg width="32" height="32" fill="none" stroke="#333" stroke-width="1.5"><path d="M6 14a10 8 0 0 1 20 0zM16 14v14M4 28c4-3 8-3 12 0s8 3 12 0"/></svg>First line to the sea</div>
  <div class="feature" style="left:232px;top:30px">
    <svg width="32" height="32" fill="none" stroke="#333" stroke-width="1.5"><path d="M4 24h24M8 24V10h16v14M8 14h16M4 28c4-3 8-3 12 0s8 3 12 0"/></svg>Aquapark</div>
  <div class="feature active" style="left:418px;top:22px;height:162px">
    <svg width="32" height="32" fill="none" stroke="#a5103b" stroke-width="1.5"><path d="M4 26V10M4 20h24v6M8 20v-6h8v6M28 26v-6"/></svg>Luxurious rooms</div>
  <div class="feature" style="left:604px;top:30px">
    <svg width="32" height="32" fill="none" stroke="#333" stroke-width="1.5"><path d="M6 6h20L16 18zM16 18v10M10 28h12"/></svg>Restaurants &amp; Bars</div>
  <div class="feature" style="left:44px;top:180px">
    <svg width="32" height="32" fill="none" stroke="#333" stroke-width="1.5"><circle cx="16" cy="7" r="3"/><path d="M16 11v8M8 18l8-4 8 4M6 26h20M10 26l6-7 6 7"/></svg>Relax and<br>Wellness center</div>
  <div class="feature" style="left:232px;top:180px">
    <svg width="32" height="32" fill="none" stroke="#333" stroke-width="1.5"><path d="M10 16h12M6 10v12M10 8v16M22 8v16M26 10v12"/></svg>Fitness Center</div>
  <div class="feature" style="left:418px;top:180px">
    <svg width="32" height="32" fill="none" stroke="#333" stroke-width="1.5"><circle cx="12" cy="8" r="4"/><circle cx="20" cy="12" r="4"/><circle cx="16" cy="22" r="6"/></svg>Bowling Center</div>
  <div class="feature" style="left:604px;top:180px">
    <svg width="32" height="32" fill="none" stroke="#333" stroke-width="1.5"><circle cx="10" cy="16" r="6"/><circle cx="22" cy="16" r="6"/><path d="M4 26h24"/></svg>Kids club</div>
</div>

<!-- accommodation -->
<div class="abs center eyebrow" style="top:3970px">Extra Features</div>
<h2 class="abs center heading section-title" style="top:4016px">Our Accommodation</h2>

<div class="room" style="left:184px">
  <div class="photo" style="left:0;top:0;width:204px;height:275px;background:linear-gradient(160deg,#ece9e4,#d9d2c9 55%,#f4f1ec)" role="img" aria-label="Studio room with white bed and framed prints"></div>
  <div class="info" style="left:228px">
    <h4>Studio</h4>
    <div class="rate-line">$199/<small>Per Night</small> &nbsp;<b style="font-size:12px">35 sq.m.</b></div>
    <ul><li>king size bed</li><li>kitchenette</li><li>SAT TV</li><li>central AC</li><li>Balcony/Terrace</li></ul>
    <div class="more">View More</div>
  </div>
</div>
<div class="room" style="left:611px">
  <div class="photo" style="left:0;top:0;width:201px;height:275px;background:linear-gradient(160deg,#f1efec,#d6d8dc 55%,#f6f4f1)" role="img" aria-label="Bright apartment bedroom with ceiling fan"></div>
  <div class="info" style="left:201px;top:0;width:204px;height:275px;background:var(--gold);color:#fff;padding:28px 0 0 26px">
    <h4>One Bedroom<br>Apartment</h4>
    <div class="rate-line">$199/<small>Per Night</small> &nbsp;<b style="font-size:12px">50 sq.m.</b></div>
    <ul><li>king size bed</li><li>kitchenette</li><li>SAT TV</li><li>central AC</li></ul>
    <div class="more" style="border-color:#fff">View More</div>
  </div>
</div>
<div class="btn" style="left:529px;top:4426px;width:142px;height:50px">View More</div>

<!-- footer -->
<div class="abs footer"></div>
<div class="abs news-title">Get update by signup<br>Newsletter.</div>
<div class="abs news-box">
  <svg class="abs" style="left:40px;top:29px" width="16" height="12" fill="none" stroke="#555" stroke-width="1.5"><rect x="1" y="1" width="14" height="10"/><path d="M1 1l7 6 7-6"/></svg>
  <span class="abs" style="left:74px;top:25px;color:#999;font-size:14px">Enter your email</span>
  <div class="btn" style="left:300px;top:11px;width:114px;height:48px;box-shadow:none">Subscribe</div>
</div>

<div class="abs brand" style="left:184px;top:4810px;font-size:17px"><span class="dot" style="margin:0 8px 0 0;width:12px;height:12px"></span>Coral Bay Resort</div>
<p class="abs" style="left:184px;top:4866px;width:190px;font-size:11px;line-height:1.6;color:#ddd">Lorem ipsum dolor sit amet, con secteteur adipisicing.</p>
<div class="abs" style="left:184px;top:4924px"><i class="dot" style="margin:0 10px 0 0"></i><i class="dot" style="margin:0 10px 0 0"></i><i class="dot" style="margin:0 10px 0 0"></i><i class="dot" style="margin:0"></i></div>

<div class="col" style="left:500px"><h5>Quick Links</h5><div>Coral Bay Resort</div><div>Book direct</div><div>Special Offers</div><div>Location</div></div>
<div class="col" style="left:658px"><h5>Help</h5><div>Log in</div><div>Blog</div><div>Contact</div><div>Privacy policy</div></div>
<div class="col" style="left:804px;width:220px"><h5>Contact Us</h5>
  <div class="contact-row"><span class="ico">&#9742;</span><span>+00 555 0199 00</span></div>
  <div class="contact-row"><span class="ico">&#9993;</span><span>hello@coralbayresort.example</span></div>
  <div class="contact-row" style="line-height:1.6">
    <span class="ico"><svg width="10" height="13" style="margin-top:3px"><path d="M5 12C1 7 1 5 1 5a4 4 0 0 1 8 0s0 2-4 7z" fill="#fff"/></svg></span>
    <span>Coral Bay Resort, 14 Harbour Lane<br>8100 Saltmere</span></div>
</div>
<div class="abs copy">Copyright © 2021 www.coralbayresort.example All rights reserved</div>

</body>
</html>
```